Business Card Design for Concierge business

Hi. I would like to have an elegant, smart business card for my concierge business, called Harbor Concierge. The services I provide are mail management, dog walking, cleaning, car, stylist, personal shopper, running errands, property management, event planning. I was thinking to add my picture but I would like to see options without it as well, if possible.

Thank you.

Business Card Details:
*Designers are to solely use contact information for the business card design. This is not to be used to contact the customer*

Name: Mirela Dobos
mail: tidewayconcierge@mailvista.example
Phone: 555-284-1097

Target Market(s)

vacation home owners

Industry/Entity Type

Business

Font styles to use
Serif

Colors

Designer to choose colors to be used in the design.

Requirements
Nice to have
• Could use icons that describe the services I provide for example car, house, key, shopping cart, shopping bags, envelope, champagne glasses, phone, dog etc.

```html
<!DOCTYPE html>
<html lang="en">
<head>
<meta charset="utf-8">
<title>Harbor Concierge – Business Card</title>
<link href="https://fonts.googleapis.com/css2?family=Cormorant+Garamond:wght@600&family=PT+Sans:wght@400&display=swap" rel="stylesheet">
<style>
  :root {
    --backdrop: #6f6f6f;
    --backdrop-top: #666666;
    --card-tan: #ad9072;
    --photo-light: #cdb89c;
    --photo-mid: #bfa686;
    --ink: #121212;
    --band-dark: #151515;
    --card-black: #050507;
    --accent: #e6c79f;
    --band-light: #dcc0a0;
    --list-text: #f1dcc0;
  }
  * { margin: 0; padding: 0; box-sizing: border-box; }
  html, body { width: 1200px; height: 900px; overflow: hidden; }
  body {
    position: relative;
    background: linear-gradient(180deg, var(--backdrop-top) 0%, var(--backdrop) 100%);
    font-family: "PT Sans", sans-serif;
  }
  .card {
    position: absolute;
    top: 306px;
    width: 440px;
    height: 271px;
    border-radius: 10px;
    overflow: hidden;
    box-shadow: 0 2px 6px rgba(0,0,0,0.25);
  }
  .card--front { left: 149px; background: var(--card-tan); }
  .card--back { left: 608px; width: 441px; background: var(--card-black); }

  .portrait {
    position: absolute;
    left: 0; top: 0;
    width: 200px; height: 243px;
    background: linear-gradient(90deg, var(--photo-light) 0%, var(--photo-mid) 60%, var(--card-tan) 100%);
  }
  .front-band {
    position: absolute;
    left: 0; bottom: 0;
    width: 100%; height: 28px;
    background: var(--band-dark);
  }
  .brand {
    position: absolute;
    left: 201px; top: 62px;
    width: 220px;
    font-family: "Cormorant Garamond", serif;
    font-weight: 600;
    font-size: 28px;
    line-height: 32px;
    color: var(--ink);
    white-space: nowrap;
  }
  .holder {
    position: absolute;
    left: 210px; top: 157px;
    font-family: "Cormorant Garamond", serif;
    font-weight: 600;
    font-size: 19px;
    letter-spacing: 0.8px;
    font-variant: small-caps;
    color: var(--ink);
  }
  .contact {
    position: absolute;
    left: 210px; top: 196px;
    list-style: none;
    font-size: 12px;
    line-height: 16px;
    color: var(--ink);
  }
  .contact li { display: flex; align-items: center; gap: 5px; white-space: nowrap; }
  .contact svg { width: 9px; height: 9px; flex: none; }

  .services-title {
    position: absolute;
    left: 41px; top: 84px;
    font-size: 22px;
    font-weight: 400;
    font-variant: small-caps;
    color: var(--accent);
    letter-spacing: 0.2px;
  }
  .services {
    position: absolute;
    list-style: none;
    font-size: 15.5px;
    line-height: 20px;
    color: var(--list-text);
  }
  .services--left { left: 40px; top: 130px; }
  .services--right { left: 201px; top: 134px; }
  .services li { display: flex; align-items: center; gap: 6px; white-space: nowrap; }
  .services li::before {
    content: "";
    width: 7px; height: 7px;
    border-radius: 50%;
    background: var(--accent);
    flex: none;
  }
  .back-band {
    position: absolute;
    left: 0; bottom: 0;
    width: 100%; height: 26px;
    background: var(--band-light);
  }
</style>
</head>
<body>
  <section class="card card--front">
    <div class="portrait" role="img" aria-label="Portrait photograph of the concierge owner"></div>
    <p class="brand">Harbor Concierge</p>
    <p class="holder">Mirela Dobos</p>
    <ul class="contact">
      <li>
        <svg viewBox="0 0 10 10" aria-hidden="true"><path d="M2.2 0.6 L3.6 2.6 L2.7 3.6 Q3.6 5.6 6.4 7.3 L7.4 6.4 L9.4 7.8 L8.4 9.4 Q4.6 9.4 0.6 1.6 Z" fill="#121212"/></svg>
        555-284-1097
      </li>
      <li>
        <svg viewBox="0 0 10 10" aria-hidden="true"><rect x="0.5" y="2" width="9" height="6.5" fill="#121212"/><path d="M0.8 2.4 L5 5.6 L9.2 2.4" stroke="#ad9072" stroke-width="0.9" fill="none"/></svg>
        tidewayconcierge@mailvista.example
      </li>
    </ul>
    <div class="front-band"></div>
  </section>

  <section class="card card--back">
    <h2 class="services-title">Our Services</h2>
    <ul class="services services--left">
      <li>Mail Management</li>
      <li>Dog Walking</li>
      <li>Cleaning</li>
      <li>Car</li>
      <li>Stylist</li>
    </ul>
    <ul class="services services--right">
      <li>Personal Shopper</li>
      <li>Running Errands</li>
      <li>Property Management</li>
      <li>Event Planning</li>
    </ul>
    <div class="back-band"></div>
  </section>
</body>
</html>
```